Create a new website for "The Arcade at Fernbrook"

I need a website for a shopping center in Atlanta USA. I want a classy high end look with high end motion videos (which I will provide).
The purpose of website is to attract new tenants to fill up vacant office spaces we have.
we will highlight existing cool stores and advertise that this is a cool place to start a new tenants business or office . ideally IT businesses in Alpharetta city in Georgia state in USA

Target Market(s)

commercial office tenants

Industry/Entity Type

Real Estate

Contact Information for Business Card

classy high end design
Arcade at Fernbrook
address:
2870 Briarwell Pkwy
Alpharetta GA 30005

Logo Text

I am open. Anything that attracts new IT tech tenants to lease up shopping center/ office space

Coding

Coded - Design and coding required

Number of Pages Required

5+ page

Requirements
Must have
• easy to browse

here is a link to some photos. i will provide videos shortly

http://www.tomsereph.com/2014/04/Building-Photos-3/n-5N2dg/
Nice to have
• please look at some of mall websites i like. Moving videos and images on home page

I really like this one: https://www.plazaatcresthollow.com/

others are

https://lindorecenter.com/

https://www.discoverbrisket.com/

```html
<!DOCTYPE html>
<html lang="en">
<head>
<meta charset="utf-8">
<title>The Arcade at Fernbrook</title>
<link rel="stylesheet" href="https://fonts.googleapis.com/css2?family=Montserrat:ital,wght@0,400;0,500;0,600;0,700;0,800;1,600&display=swap">
<style>
:root{
  --ink:#111111;
  --text:#333333;
  --muted:#555555;
  --red:#e3241b;
  --topbar:#262626;
  --header:#000000;
  --soft:#f4f4f4;
  --tile:#ececec;
  --line:#222222;
  --footer:#1b1b1b;
  --white:#ffffff;
}
*{box-sizing:border-box;margin:0;padding:0}
html,body{width:1200px;height:4877px;overflow:hidden}
body{position:relative;font-family:'Montserrat',sans-serif;color:var(--text);background:var(--white)}
.abs{position:absolute}
.center{left:0;width:1200px;text-align:center}
.section-title{font-size:38px;font-weight:500;letter-spacing:5px;color:var(--ink);line-height:44px}
.btn{position:absolute;display:flex;align-items:center;justify-content:center;border:2px solid var(--line);font-size:15px;font-weight:700;letter-spacing:1px;color:var(--ink);background:transparent}
.btn.light{border-color:var(--white);color:var(--white)}
.photo{position:absolute}

/* top bar */
.topbar{top:0;left:0;width:1200px;height:42px;background:var(--topbar);color:#ddd;font-size:13px}
.topbar .item{position:absolute;top:13px;display:flex;align-items:center;gap:7px}
.social{position:absolute;top:10px;display:flex;gap:8px;right:158px}
.social span{width:22px;height:22px;border-radius:50%;background:var(--white)}

/* header */
.header{top:42px;left:0;width:1200px;height:113px;background:var(--header)}
.brand{position:absolute;top:18px;left:0;width:1200px;text-align:center;font-size:33px;font-weight:500;color:var(--white);letter-spacing:1px}
.nav{position:absolute;top:76px;left:0;width:1200px;display:flex;justify-content:center;align-items:center;gap:22px;color:var(--white);font-size:14px;font-weight:500;letter-spacing:.5px}
.nav .sep{font-size:12px;color:#bbb}

/* hero */
.hero{top:155px;left:0;width:1200px;height:483px;background:linear-gradient(180deg,#5b6775 0%,#7b8694 22%,#8c7f6e 42%,#a8977c 55%,#6e5a48 68%,#8d8f93 80%,#c3c6ca 88%,#5a5c60 100%)}
.hero-title{top:300px;font-size:86px;font-weight:800;letter-spacing:14px;color:var(--white);line-height:100px;text-shadow:0 2px 8px rgba(0,0,0,.25)}
.hero-sub{top:410px;font-size:26px;font-weight:700;letter-spacing:5px;color:var(--white)}

/* stores */
.store-tile{position:absolute;top:748px;width:136px;height:134px;background:var(--tile);display:flex;align-items:center;justify-content:center;font-size:14px;font-weight:600;color:#3b4d5e;text-align:center}
.arrow{position:absolute;top:805px}

/* whats new */
.news{top:1015px;left:0;width:1200px;height:1168px;background:var(--soft)}
.card-title{position:absolute;font-size:25px;font-weight:700;color:var(--ink);letter-spacing:.5px;line-height:30px}
.card-text{position:absolute;font-size:14px;line-height:19px;color:var(--muted)}
.floor-tag{position:absolute;top:1827px;left:157px;width:152px;height:51px;background:#1f1f1f;color:var(--white);font-size:26px;font-weight:600;letter-spacing:1px;display:flex;align-items:center;justify-content:center}
.dots{position:absolute;display:flex;gap:6px}
.dots span{width:10px;height:10px;border-radius:50%;border:1.5px solid var(--white)}
.dots span.on{background:var(--white)}

/* banner */
.banner{top:2183px;left:0;width:1200px;height:562px;background:linear-gradient(180deg,#0b1530 0%,#18264a 30%,#2a3552 48%,#6b5236 60%,#3a2f28 68%,#232326 82%,#151517 100%)}
.banner-kicker{top:2344px;font-size:40px;font-weight:700;letter-spacing:3px;color:var(--white)}
.banner-kicker em{font-style:normal;color:var(--red)}
.banner-title{top:2392px;font-size:70px;font-weight:800;letter-spacing:9px;color:var(--white);line-height:70px}

/* blog */
.post-cat{position:absolute;top:3180px;font-size:12px;font-weight:600;font-style:italic;letter-spacing:1px;color:#444}
.post-title{position:absolute;top:3196px;width:280px;font-size:20px;font-weight:600;line-height:24px;color:var(--ink)}
.post-text{position:absolute;top:3248px;width:255px;font-size:13.5px;line-height:19px;color:var(--muted)}
.post-more{position:absolute;top:3318px;font-size:14px;font-weight:700;letter-spacing:2px;color:var(--red)}

/* insider */
.insider{top:3493px;left:0;width:1200px;height:526px;background:linear-gradient(180deg,#232323 0%,#1c1c1c 55%,#2e2e2e 80%,#242424 100%)}
.insider-title{top:3560px;font-size:38px;font-weight:500;letter-spacing:4px;color:var(--white)}
.insider-sub{top:3613px;font-size:18px;color:#e6e6e6}
.field{position:absolute;background:var(--white);border:1px solid #ccc;height:43px;font-size:13px;color:#666;display:flex;align-items:center;padding-left:14px}
.interest{position:absolute;left:273px;font-size:15px;color:#e6e6e6;display:flex;align-items:center;gap:8px}
.interest i{width:10px;height:10px;border:1px solid #ccc;display:inline-block}
.btn-red{position:absolute;background:var(--red);color:var(--white);font-size:15px;font-weight:700;letter-spacing:1px;display:flex;align-items:center;justify-content:center}

/* footer */
.footer{top:4500px;left:0;width:1200px;height:377px;background:var(--footer);color:#ddd}
.f-head{position:absolute;top:4607px;font-size:16px;font-weight:600;color:var(--white);letter-spacing:.5px}
.f-link{position:absolute;font-size:14px;color:#ddd}
.f-hours{position:absolute;font-size:14px;color:#ddd;line-height:24px}
.f-hours b{color:var(--white);font-weight:700}
</style>
</head>
<body>

<!-- Top bar -->
<div class="abs topbar">
  <div class="item" style="left:157px">
    <svg width="15" height="15" viewBox="0 0 16 16"><circle cx="8" cy="8" r="6.5" fill="none" stroke="#ddd" stroke-width="1.5"/><path d="M8 4v4l3 2" fill="none" stroke="#ddd" stroke-width="1.5"/></svg>
    Todays Hours 10 AM - 9 PM
  </div>
  <div class="item" style="left:388px">
    <svg width="12" height="16" viewBox="0 0 12 16"><path d="M6 0C2.7 0 0 2.6 0 5.9 0 10.3 6 16 6 16s6-5.7 6-10.1C12 2.6 9.3 0 6 0zm0 8.3a2.4 2.4 0 110-4.8 2.4 2.4 0 010 4.8z" fill="#ddd"/></svg>
    2870 Briarwell Pkwy Alpharetta GA 30005
  </div>
  <div class="social"><span></span><span></span><span></span><span></span></div>
</div>

<!-- Header -->
<header class="abs header">
  <div class="brand">THE ARCADE AT FERNBROOK</div>
  <nav class="nav">
    <span>HOME</span><span class="sep">I</span>
    <span>DIRECTORY</span><span class="sep">I</span>
    <span>ABOUT</span><span class="sep">I</span>
    <span>BLOG</span><span class="sep">I</span>
    <span>CONTACT</span><span class="sep">I</span>
    <svg width="13" height="13" viewBox="0 0 14 14"><circle cx="6" cy="6" r="4.5" fill="none" stroke="#fff" stroke-width="2"/><path d="M9.5 9.5L13 13" stroke="#fff" stroke-width="2"/></svg>
  </nav>
</header>

<!-- Hero -->
<section class="abs hero" role="img" aria-label="Dusk view of the shopping center storefronts with parked cars"></section>
<h1 class="abs center hero-title">FERNBROOK</h1>
<p class="abs center hero-sub">A SHOPPING CENTER IN ATLANTA USA</p>

<!-- Check store -->
<h2 class="abs center section-title" style="top:690px">CHECK STORE</h2>
<svg class="arrow" style="left:141px" width="10" height="16" viewBox="0 0 10 16"><path d="M8 2L2 8l6 6" fill="none" stroke="#aaa" stroke-width="1.5"/></svg>
<div class="store-tile" style="left:157px">Birchline</div>
<div class="store-tile" style="left:307px">Clearpoint</div>
<div class="store-tile" style="left:457px">Tallyhouse</div>
<div class="store-tile" style="left:607px">Harbor Crest</div>
<div class="store-tile" style="left:757px">Marlowe Advisors</div>
<div class="store-tile" style="left:907px">Bluefin Row</div>
<svg class="arrow" style="left:1050px" width="10" height="16" viewBox="0 0 10 16"><path d="M2 2l6 6-6 6" fill="none" stroke="#aaa" stroke-width="1.5"/></svg>
<div class="btn" style="left:509px;top:905px;width:180px;height:49px">VIEW DIRECTORY</div>

<!-- What's new -->
<section class="abs news"></section>
<h2 class="abs center section-title" style="top:1057px">WHATS ‘ NEW</h2>

<div class="photo" style="left:157px;top:1130px;width:511px;height:451px;background:linear-gradient(180deg,#f1f0ec 0%,#e4e2dc 28%,#b9b6b0 45%,#d8d4cc 60%,#8c90a8 78%,#5d6688 100%)" role="img" aria-label="Boutique interior with clothing racks and hanging plants"></div>
<div class="card-title" style="left:157px;top:1594px">BOUTIQUES</div>
<div class="card-text" style="left:157px;top:1627px;width:445px">Tech teams leasing here share the center with boutiques that keep the walkways lively all day long.</div>
<div class="btn" style="left:157px;top:1698px;width:136px;height:46px">DETAILS</div>

<div class="photo" style="left:682px;top:1130px;width:361px;height:299px;background:linear-gradient(180deg,#2f6fb3 0%,#4f8ccb 30%,#c9b89c 40%,#a7753d 62%,#6b4526 82%,#3d2c22 100%)" role="img" aria-label="Bakery and deli storefront at dusk"></div>
<div class="card-title" style="left:682px;top:1443px">DINING</div>
<div class="card-text" style="left:682px;top:1476px;width:360px">Cafes and delis sit steps from your office, so client lunches and team breaks never mean a drive.</div>
<div class="btn" style="left:682px;top:1539px;width:136px;height:47px">DETAILS</div>

<div class="photo" style="left:682px;top:1656px;width:361px;height:298px;background:linear-gradient(120deg,#2f2c2e 0%,#6d5444 30%,#d9b98e 52%,#efe0c8 62%,#8a6e58 80%,#3b3433 100%)" role="img" aria-label="Shopper browsing clothing in a store"></div>
<div class="card-title" style="left:682px;top:1967px">BY DESIGN</div>
<div class="card-text" style="left:682px;top:1996px;width:360px">Flexible suites can be fitted out for studios, labs and IT firms ready to grow in Alpharetta.</div>
<div class="btn" style="left:682px;top:2071px;width:136px;height:47px">DETAILS</div>

<div class="photo" style="left:157px;top:1795px;width:511px;height:331px;background:linear-gradient(180deg,#e0a93c 0%,#f0e3c8 30%,#fbf7ee 48%,#c98a4e 66%,#9a5425 84%,#6a3318 100%)" role="img" aria-label="Vacant office suite with glass partitions and polished floor, available to lease"></div>
<div class="floor-tag">FLOOR</div>
<div class="dots" style="left:176px;top:2100px"><span class="on"></span><span></span><span></span><span></span><span></span></div>

<!-- Banner -->
<section class="abs banner" role="img" aria-label="Shopping center at night under a deep blue sky"></section>
<p class="abs center banner-kicker">A <em>SHOPPING CENTER</em> IN</p>
<p class="abs center banner-title">ATLANTA USA</p>
<div class="btn light" style="left:536px;top:2474px;width:130px;height:46px">ABOUT US</div>
<div class="dots" style="left:563px;top:2704px"><span class="on"></span><span></span><span></span><span></span><span></span></div>

<!-- Blog -->
<h2 class="abs center section-title" style="top:2799px">BLOG</h2>

<div class="photo" style="left:157px;top:2853px;width:284px;height:303px;background:linear-gradient(115deg,#d9d4c8 0%,#bdb6a8 35%,#4b6fae 55%,#86a6d6 70%,#a39d93 85%,#8a5246 100%)" role="img" aria-label="Corner storefront of a retail building"></div>
<div class="post-cat" style="left:157px">OFFICE LEASING</div>
<div class="post-title" style="left:157px">Office suites open for tech teams</div>
<div class="post-text" style="left:157px">Bright, move-in ready suites sized for startups and IT firms, with parking right outside . . .</div>
<div class="post-more" style="left:157px">LEARN MORE</div>

<div class="photo" style="left:458px;top:2853px;width:284px;height:303px;background:linear-gradient(100deg,#e9e6e1 0%,#c9b3a4 30%,#c8323a 48%,#b42a33 56%,#d8d3cc 72%,#9b9aa0 100%)" role="img" aria-label="Friends carrying shopping bags in a mall"></div>
<div class="post-cat" style="left:458px">OFFICE LEASING</div>
<div class="post-title" style="left:458px">Why IT firms pick Alpharetta</div>
<div class="post-text" style="left:458px">A deep tech talent pool, easy GA 400 access and shops on site make hiring and daily life simpler . . .</div>
<div class="post-more" style="left:458px">LEARN MORE</div>

<div class="photo" style="left:757px;top:2853px;width:284px;height:303px;background:linear-gradient(180deg,#3f7fd0 0%,#8fb6e6 30%,#f2f0ea 50%,#dcd7cd 68%,#9a948b 82%,#b8a49a 100%)" role="img" aria-label="White clock tower building in the shopping center"></div>
<div class="post-cat" style="left:757px">OFFICE LEASING</div>
<div class="post-title" style="left:757px">Flexible floors, ready to move in</div>
<div class="post-text" style="left:757px">Open plans or private rooms, short or long terms, our leasing team shapes the space around you . . .</div>
<div class="post-more" style="left:757px">LEARN MORE</div>

<div class="btn" style="left:532px;top:3387px;width:134px;height:45px">VIEW ALL</div>

<!-- Mall insider -->
<section class="abs insider" role="img" aria-label="Darkened parking lot in front of the center"></section>
<h2 class="abs center insider-title">BECOME A MALL INSIDER TODAY.</h2>
<p class="abs center insider-sub">Join our email list for the latest news from The Galleria at Westmoor.</p>
<div class="field" style="left:273px;top:3656px;width:320px">Name :</div>
<div class="field" style="left:608px;top:3656px;width:321px">Email :</div>
<div class="field" style="left:273px;top:3714px;width:656px;height:47px">Language :
  <svg style="position:absolute;right:14px;top:20px" width="10" height="7" viewBox="0 0 10 7"><path d="M0 0h10L5 7z" fill="#444"/></svg>
</div>
<div class="abs" style="left:273px;top:3780px;font-size:16px;color:#e6e6e6">What are you interested in hearing about?</div>
<div class="interest" style="top:3806px"><i></i>Boutiques</div>
<div class="interest" style="top:3830px"><i></i>Dining</div>
<div class="interest" style="top:3855px"><i></i>Designs</div>
<div class="interest" style="top:3879px"><i></i>Promotions</div>
<div class="btn-red" style="left:795px;top:3850px;width:134px;height:44px">SUBMIT</div>

<!-- Snapgram feed -->
<h2 class="abs center section-title" style="top:4071px;letter-spacing:2px">@FOLLOW US ON SNAPGRAM</h2>
<div class="photo" style="left:157px;top:4142px;width:210px;height:221px;background:linear-gradient(180deg,#7ea6db 0%,#b9cbe3 30%,#e4ded2 50%,#a08468 75%,#5e4a3a 100%)" role="img" aria-label="Bakery storefront building"></div>
<div class="photo" style="left:382px;top:4142px;width:211px;height:221px;background:linear-gradient(160deg,#a3a6a5 0%,#6b6f70 35%,#2f3234 55%,#8d8e8a 75%,#c2c1bb 100%)" role="img" aria-label="Aerial view of a full parking lot"></div>
<div class="photo" style="left:608px;top:4142px;width:210px;height:221px;background:linear-gradient(160deg,#c03a86 0%,#e05aa6 40%,#a2306c 70%,#6e1f48 100%)" role="img" aria-label="Empty unit with bright pink walls"></div>
<div class="photo" style="left:833px;top:4142px;width:210px;height:221px;background:linear-gradient(180deg,#d5dfea 0%,#b9c2ca 30%,#c4ad8c 55%,#8d7a62 78%,#5e554c 100%)" role="img" aria-label="Storefront building behind bare winter trees"></div>
<div class="btn" style="left:532px;top:4394px;width:134px;height:45px">VIEW ALL</div>

<!-- Footer -->
<footer class="abs footer"></footer>
<div class="f-head" style="left:157px">SEE ALL HOURS</div>
<svg class="abs" style="left:157px;top:4646px" width="16" height="16" viewBox="0 0 16 16"><circle cx="8" cy="8" r="6.5" fill="none" stroke="#ddd" stroke-width="1.5"/><path d="M8 4v4l3 2" fill="none" stroke="#ddd" stroke-width="1.5"/></svg>
<div class="f-hours" style="left:189px;top:4639px"><b>Monday – Saturday:</b> 10am – 9pm<br><b>Sunday:</b> 11am – 7pm</div>
<svg class="abs" style="left:157px;top:4712px" width="13" height="18" viewBox="0 0 12 16"><path d="M6 0C2.7 0 0 2.6 0 5.9 0 10.3 6 16 6 16s6-5.7 6-10.1C12 2.6 9.3 0 6 0zm0 8.3a2.4 2.4 0 110-4.8 2.4 2.4 0 010 4.8z" fill="#ddd"/></svg>
<div class="f-hours" style="left:189px;top:4705px">2870 Briarwell Pkwy<br>Alpharetta GA 30005</div>

<div class="f-head" style="left:502px">QUICK LINK</div>
<div class="f-link" style="left:502px;top:4642px">Home</div>
<div class="f-link" style="left:502px;top:4667px">Directory</div>
<div class="f-link" style="left:502px;top:4693px">About</div>
<div class="f-link" style="left:502px;top:4718px">Blog</div>
<div class="f-link" style="left:502px;top:4744px">Contact</div>

<div class="f-head" style="left:666px">CONNECT</div>
<div class="f-link" style="left:666px;top:4642px">Circlepage</div>
<div class="f-link" style="left:666px;top:4667px">Chirper</div>
<div class="f-link" style="left:666px;top:4693px">Viewtube</div>
<div class="f-link" style="left:666px;top:4718px">Snapgram</div>

<div class="f-head" style="left:808px">SIGN UP FOR LATEST NEWS</div>
<div class="field" style="left:808px;top:4648px;width:235px;justify-content:center;padding:0;color:#333">Enter Your mail</div>
<div class="btn-red" style="left:808px;top:4698px;width:235px;height:44px;font-size:14px">SUBMIT NOW</div>
<div class="f-link" style="left:808px;top:4754px">PRIVACY POLICY</div>
<div class="f-link" style="left:970px;top:4754px">SITE MAP</div>

<div class="abs center" style="top:4808px;font-size:13.5px;color:#ddd">Copyright©2020<span style="color:var(--red)">The Arcade at Fernbrook</span>. All Rights Reserved.</div>

</body>
</html>
```